Design some Stationery for Baby 1st Birthday Invitation

We require Baby's 1st Birthday party invitation. Can be be a photo card or traditional style invitation must be 5 x 7 inches plus 2.5mm bleed, can be folded or flat card.
Can be modern, contemporary, Fun must be either pink or pale blue or bright colours.

```html
<!DOCTYPE html>
<html lang="en">
<head>
<meta charset="utf-8">
<title>Happy Birthday Party Invitation</title>
<link rel="stylesheet" href="https://fonts.googleapis.com/css2?family=Rye&family=Josefin+Sans:wght@300;400;600&family=Alfa+Slab+One&display=swap">
<style>
  :root {
    --magenta: #e0358f;
    --pink: #ec4f9b;
    --blush: #f6c6dc;
    --stripe-light: #fbe3ee;
    --stripe-dark: #f5cadf;
    --purple: #8c55b4;
    --purple-deep: #6e3d94;
    --pink-deep: #c42a7a;
    --paper: #fdfbfc;
    --grey: #7a7478;
    --pale-text: #f4b3cf;
    --stage: #2a2a2e;
  }
  * { margin: 0; padding: 0; box-sizing: border-box; }
  html, body { width: 1200px; height: 900px; overflow: hidden; background: var(--stage); }
  .canvas { position: relative; width: 1200px; height: 900px; }

  .invitation {
    position: absolute; left: 293px; top: 40px; width: 615px; height: 820px;
    background: var(--blush);
    font-family: "Josefin Sans", sans-serif;
  }
  .invitation__frame {
    position: absolute; inset: 10px;
    border: 5px solid var(--magenta);
    background: var(--paper);
  }
  .invitation__dashed {
    position: absolute; inset: 8px;
    border: 2px dashed var(--pink);
  }
  .stripes {
    background: repeating-linear-gradient(90deg, var(--stripe-dark) 0 24px, var(--stripe-light) 24px 48px);
  }
  .top-band { position: absolute; left: 30px; top: 27px; }
  .bottom-band { position: absolute; left: 30px; top: 735px; width: 555px; height: 50px; }

  .headline {
    position: absolute; left: 0; right: 0; text-align: center;
    font-family: "Rye", serif; line-height: 1; letter-spacing: 1px;
  }
  .headline--happy { top: 160px; font-size: 56px; color: var(--pink); text-shadow: 0 2px 0 var(--pink-deep); }
  .headline--birthday { top: 224px; font-size: 62px; color: var(--purple); text-shadow: 0 2px 0 var(--purple-deep); }
  .headline--party { top: 294px; font-size: 50px; color: var(--pink); text-shadow: 0 2px 0 var(--pink-deep); }

  .rule { position: absolute; left: 30px; width: 555px; border-top: 1.5px solid var(--pink); }
  .rule--double { top: 392px; height: 5px; border-bottom: 1px dashed var(--pink); }
  .rule--star { top: 578px; }

  .join-us {
    position: absolute; left: 40px; top: 438px;
    font-size: 66px; font-weight: 400; color: var(--purple); letter-spacing: 2px; line-height: 1;
  }
  .date { position: absolute; right: 48px; top: 438px; text-align: right; color: var(--pink); line-height: 1.1; }
  .date__day { font-size: 32px; letter-spacing: 3px; }
  .date__full { font-size: 22px; letter-spacing: 2px; }

  .tagline {
    position: absolute; left: 0; right: 0; top: 538px; text-align: center;
    font-size: 23px; letter-spacing: 3px; color: var(--grey); font-weight: 300;
  }

  .photo-slot {
    position: absolute; left: 40px; top: 600px; width: 200px; height: 112px;
    background: var(--paper); border: 3px solid var(--stripe-dark);
    display: flex; align-items: center; justify-content: center;
    font-size: 21px; color: #333; letter-spacing: 1px;
  }

  .host { position: absolute; right: 48px; top: 610px; text-align: right; }
  .host__label { font-family: "Alfa Slab One", serif; font-size: 21px; color: var(--magenta); letter-spacing: 1px; }
  .host__details { margin-top: 18px; font-size: 19px; color: var(--pale-text); letter-spacing: 2px; line-height: 1.2; }
</style>
</head>
<body>
<div class="canvas">
  <div class="invitation">
    <div class="invitation__frame">
      <div class="invitation__dashed"></div>
    </div>

    <svg class="top-band" width="555" height="135" viewBox="0 0 555 135" aria-hidden="true">
      <defs>
        <pattern id="band-stripes" width="48" height="10" patternUnits="userSpaceOnUse">
          <rect width="24" height="10" fill="#f5cadf"/>
          <rect x="24" width="24" height="10" fill="#fbe3ee"/>
        </pattern>
        <path id="invite-arc" d="M 110 132 Q 277 60 445 132"/>
      </defs>
      <path d="M0 0 H555 V132 Q277 60 0 132 Z" fill="url(#band-stripes)"/>
      <text font-family="Josefin Sans, sans-serif" font-size="20" fill="#ec4f9b" letter-spacing="2">
        <textPath href="#invite-arc" startOffset="50%" text-anchor="middle">YOU ARE INVITED TO</textPath>
      </text>
    </svg>

    <div class="headline headline--happy">HAPPY</div>
    <div class="headline headline--birthday">BIRTHDAY</div>
    <div class="headline headline--party">PARTY</div>

    <div class="rule rule--double"></div>

    <div class="join-us">JOIN US</div>
    <div class="date">
      <div class="date__day">SATURDAY</div>
      <div class="date__full">OCTOBER 12, 2013</div>
    </div>

    <div class="tagline">BIRTHDAY FUN, FOOD AND GAMES</div>

    <div class="rule rule--star"></div>
    <svg style="position:absolute;left:297px;top:568px" width="20" height="20" viewBox="0 0 20 20" aria-hidden="true">
      <rect width="20" height="20" fill="#fdfbfc"/>
      <polygon points="10,2 12.4,7.6 18.5,8 13.8,12 15.3,18 10,14.7 4.7,18 6.2,12 1.5,8 7.6,7.6" fill="none" stroke="#ec4f9b" stroke-width="1.3"/>
    </svg>

    <div class="photo-slot" role="img" aria-label="Space for the birthday child's photo">PHOTO HERE</div>
    <svg style="position:absolute;left:40px;top:600px" width="200" height="112" viewBox="0 0 200 112" aria-hidden="true">
      <polygon points="178,0 200,0 200,22" fill="#e0358f"/>
      <polygon points="0,90 0,112 22,112" fill="#e0358f"/>
    </svg>

    <div class="host">
      <div class="host__label">INVITED BY</div>
      <div class="host__details">YOUR NAME<br>ADDRESS</div>
    </div>

    <div class="bottom-band stripes"></div>
  </div>
</div>
</body>
</html>
```